Reverse Mortgage company needs a Facebook design

We need a facebook design for a mortgage company based in Orange County California. I started the facebook page at https://www.examplesocial.test/Tidewaterlendingandtrust. We specialize in mortgage financing and our main focus is Reverse Mortgages. We would like to see a design that would incorporate our existing color scheme on the loanbridgeready.test website. The design should be tailored for homeowners 62 years of age and older.
Updates
The DUNE inc jpg file that I uploaded is the logo that we use. The 2nd jpg that I uploaded was just to give you a better image of the graphic. Thank you
Target Market(s)
American Homeowners age 62 and older
Industry/Entity Type
It Company
Colors
Designer to choose colors to be used in the design.
Look and feel
Each slider illustrates characteristics of the customer's brand and the style your logo design should communicate.

```html
<!DOCTYPE html>
<html lang="en">
<head>
<meta charset="utf-8">
<title>DUNE inc – Reverse Mortgages</title>
<link href="https://fonts.googleapis.com/css2?family=Arimo:wght@400;700&display=swap" rel="stylesheet">
<style>
  :root {
    --page-bg: #e6e6e6;
    --banner-bg: #ffffff;
    --ink: #222222;
    --brand-green: #789a3c;
    --swoosh-black: #1c1c1c;
    --photo-light: #eef0ec;
    --photo-mid: #c9cdc4;
    --photo-warm: #d9cfc4;
  }
  * { margin: 0; padding: 0; box-sizing: border-box; }
  html, body {
    width: 1200px;
    height: 445px;
    overflow: hidden;
    background: var(--page-bg);
    font-family: "Arimo", Arial, sans-serif;
  }
  .canvas {
    position: relative;
    width: 1200px;
    height: 445px;
  }
  .cover-banner {
    position: absolute;
    left: 87px;
    top: 14px;
    width: 1025px;
    height: 380px;
    background: var(--banner-bg);
    overflow: hidden;
  }
  .brand {
    position: absolute;
    left: 52px;
    top: 50px;
  }
  .brand-name {
    font-size: 68px;
    font-weight: 700;
    color: var(--ink);
    line-height: 1;
    letter-spacing: 1px;
  }
  .brand-tagline {
    margin-top: 10px;
    font-size: 15px;
    font-weight: 400;
    color: var(--ink);
    letter-spacing: 0.4px;
  }
  .headline {
    position: absolute;
    left: 55px;
    top: 178px;
    font-size: 31px;
    font-weight: 700;
    color: var(--brand-green);
    letter-spacing: -0.3px;
  }
  .hero-photo {
    position: absolute;
    left: 445px;
    top: 0;
    width: 510px;
    height: 315px;
    background:
      radial-gradient(ellipse at 55% 45%, var(--photo-warm) 0%, var(--photo-mid) 40%, rgba(255,255,255,0) 75%),
      linear-gradient(90deg, rgba(255,255,255,1) 0%, var(--photo-light) 25%, var(--photo-light) 85%, rgba(255,255,255,1) 100%);
  }
  .swoosh {
    position: absolute;
    left: 0;
    top: 0;
    width: 1025px;
    height: 380px;
  }
</style>
</head>
<body>
  <div class="canvas">
    <section class="cover-banner">
      <div class="hero-photo" role="img" aria-label="Photo of a smiling senior couple looking at a laptop together"></div>

      <svg class="swoosh" viewBox="0 0 850 315" preserveAspectRatio="none" aria-hidden="true">
        <path d="M0,292 C300,300 600,232 850,142 L850,315 L0,315 Z" fill="var(--brand-green)"/>
        <path d="M0,276 C300,290 600,202 850,104 L850,122 C600,216 300,292 0,282 Z" fill="var(--swoosh-black)"/>
      </svg>

      <div class="brand">
        <div class="brand-name">DUNE inc</div>
        <div class="brand-tagline">Tidewater Lending and Trust.test</div>
      </div>

      <h1 class="headline">Reverse Mortgages</h1>
    </section>
  </div>
</body>
</html>
```